Folded A4 flyer for design&construction company

Folded A4 flyer needed. Keywords: elegant, stylish
our website www.corvimo.ae

Industry/Entity Type

Construction

```html
<!DOCTYPE html>
<html lang="en">
<head>
<meta charset="utf-8">
<title>Corvimo – Design & Construction Flyer</title>
<link href="https://fonts.googleapis.com/css2?family=Cinzel:wght@600&family=Open+Sans:wght@400;600;700&family=Playfair+Display:ital@1&display=swap" rel="stylesheet">
<style>
:root{
  --gold:#c9a13b;
  --gold-dark:#a9811f;
  --gold-light:#e6c774;
  --ink:#3a3a3a;
  --muted:#6b6b6b;
  --charcoal:#3b3b3d;
  --charcoal-dark:#2c2c2e;
  --paper:#ffffff;
  --bg:#e9e9e9;
}
*{box-sizing:border-box;margin:0;padding:0}
html,body{width:778px;height:1200px;overflow:hidden}
body{background:var(--bg);font-family:"Open Sans",Arial,sans-serif;color:var(--ink);position:relative}

.brand-name{font-family:"Cinzel",Georgia,serif;font-weight:600;color:var(--gold);letter-spacing:2px;display:flex;align-items:center;justify-content:center;gap:8px;white-space:nowrap}
.brand-dot{width:10px;height:10px;border-radius:50%;background:var(--gold)}
.brand-sub{font-family:"Playfair Display",Georgia,serif;font-style:italic;color:var(--gold-dark);text-align:center}

/* Outside sheet */
.sheet-outside{position:absolute;left:47px;top:36px;width:687px;height:521px;background:var(--paper);box-shadow:0 2px 8px rgba(0,0,0,.25);display:flex}
.panel-back{width:342px;border-right:1px solid #e3e3e3;padding:30px 28px 0;position:relative}
.panel-back .brand-name{font-size:30px;margin-top:50px}
.panel-back .brand-sub{font-size:11px;margin-bottom:12px}
.intro{font-size:9px;line-height:1.45;color:var(--muted);text-align:left}
.ornament{background:linear-gradient(90deg,transparent,var(--gold-light),var(--gold),var(--gold-light),transparent);border-radius:50%}
.panel-back .ornament{width:150px;height:26px;margin:16px auto 0;opacity:.7}
.quote-badge{position:absolute;left:32px;top:340px;width:52px;height:52px;border-radius:50%;background:#f4c21a;color:#fff;font-size:8px;font-weight:700;display:flex;align-items:center;justify-content:center;text-align:center;line-height:1.1;transform:rotate(-12deg)}
.contact{position:absolute;left:0;right:0;top:400px;text-align:center}
.contact .phone{font-size:16px;font-weight:700;color:var(--ink);display:flex;align-items:center;justify-content:center;gap:6px}
.contact .email{font-size:10px;font-weight:600;color:var(--ink);margin-top:6px}
.panel-back .web{position:absolute;left:20px;right:20px;top:460px;border-top:1px solid var(--gold-light);text-align:center;font-size:10px;color:var(--gold-dark);padding-top:6px;font-weight:600}
.address{position:absolute;left:0;right:0;top:496px;text-align:center;font-size:7px;color:var(--muted)}

.panel-front{flex:1;position:relative}
.panel-front .brand-name{font-size:46px;margin-top:82px}
.panel-front .brand-sub{font-size:15px}
.hero{position:absolute;left:34px;top:223px;width:295px;height:246px;background:linear-gradient(160deg,#f2e4c4 0%,#e9b24a 45%,#b98237 70%,#6b5438 100%)}
.hero-quote{position:absolute;left:0;right:0;bottom:8px;text-align:center;font-family:"Playfair Display",Georgia,serif;font-style:italic;font-size:11px;color:#fff}
.panel-front .web{position:absolute;left:34px;right:16px;top:477px;border-top:1px solid var(--gold-light);text-align:right;font-size:10px;color:var(--gold-dark);padding-top:6px;font-weight:600}

/* Inside sheet */
.sheet-inside{position:absolute;left:57px;top:596px;width:669px;height:571px;background:linear-gradient(180deg,var(--charcoal),var(--charcoal-dark));box-shadow:0 2px 8px rgba(0,0,0,.3)}
.gold-bar{height:64px;background:linear-gradient(180deg,var(--gold-light),var(--gold) 60%,var(--gold-dark));display:flex;justify-content:space-between;align-items:center;padding:0 22px;color:#fff;font-family:"Playfair Display",Georgia,serif;font-style:italic;font-size:15px}
.logo-tab{position:absolute;left:258px;top:4px;width:152px;height:86px;background:var(--paper);box-shadow:0 2px 6px rgba(0,0,0,.3);padding-top:20px}
.logo-tab .brand-name{font-size:22px;gap:6px}
.logo-tab .brand-dot{width:7px;height:7px}
.logo-tab .brand-sub{font-size:9px}
.photos{position:absolute;left:18px;top:92px;right:18px;height:180px;display:flex;gap:8px}
.photo{flex:1;border:2px solid #f0f0f0}
.photo.garden{background:linear-gradient(170deg,#9fc3d8,#8aa36a 55%,#c8b58e)}
.photo.room{background:linear-gradient(160deg,#efe3cc,#c99a5c 55%,#6e4a2c)}
.photo.villa{background:linear-gradient(170deg,#cfd9e3,#d8c8a8 50%,#8d7454)}
.services{position:absolute;left:18px;right:18px;top:286px;display:flex}
.service{flex:1;padding:0 6px}
.service .brand-name{font-size:22px;letter-spacing:1px}
.service .brand-sub{font-size:12px;color:var(--gold-light);margin-bottom:10px}
.service ul{list-style:none;font-size:8.5px;line-height:1.55;color:#e2e2e2;padding-left:10px}
.service li::before{content:"•";color:var(--gold);margin-right:4px}
.sheet-inside .ornament{position:absolute;left:244px;top:504px;width:180px;height:46px;opacity:.85}
</style>
</head>
<body>

<section class="sheet-outside">
  <div class="panel-back">
    <div class="brand-name"><span class="brand-dot"></span>CORVIMO</div>
    <div class="brand-sub">design &amp; construction</div>
    <p class="intro">We believe in quality beginnings and flawless finishes. We are a team of creative designers and constructors with years of experience and expertise in providing complete interior design and construction services. Our approach is founded on a commitment to excellence and quality construction. Our team specializes in classic and contemporary high quality construction in Dubai for commercial and residential projects.</p>
    <div class="ornament" role="img" aria-label="Gold flourish ornament"></div>
    <div class="quote-badge">FREE<br>QUOTE</div>
    <div class="contact">
      <div class="phone">
        <svg width="14" height="14" viewBox="0 0 24 24"><path fill="#c9a13b" d="M6.6 10.8a15 15 0 006.6 6.6l2.2-2.2c.3-.3.7-.4 1-.2 1.1.4 2.3.6 3.6.6.6 0 1 .4 1 1V20c0 .6-.4 1-1 1A17 17 0 013 4c0-.6.4-1 1-1h3.5c.6 0 1 .4 1 1 0 1.3.2 2.5.6 3.6.1.3 0 .7-.2 1z"/></svg>
        800-CORVIMO
      </div>
      <div class="email">CONTACT@CORVIMO.AE</div>
    </div>
    <div class="web">WWW.CORVIMO.AE</div>
    <div class="address">Corvimo LLC, Harbor Point Tower, Office 904, Business Bay, Dubai</div>
  </div>
  <div class="panel-front">
    <div class="brand-name"><span class="brand-dot"></span>CORVIMO</div>
    <div class="brand-sub">design &amp; construction</div>
    <div class="hero" role="img" aria-label="Photo of a luxurious curved interior with warm golden lighting">
      <div class="hero-quote">Quality is not an act, it is a habit - Darian Vell</div>
    </div>
    <div class="web">WWW.CORVIMO.AE</div>
  </div>
</section>

<section class="sheet-inside">
  <div class="gold-bar">
    <span>Customized Design Solutions...</span>
    <span>From Concept to Completion</span>
  </div>
  <div class="logo-tab">
    <div class="brand-name"><span class="brand-dot"></span>CORVIMO</div>
    <div class="brand-sub">design &amp; construction</div>
  </div>
  <div class="photos">
    <div class="photo garden" role="img" aria-label="Photo of a landscaped garden with pool"></div>
    <div class="photo room" role="img" aria-label="Photo of an elegant interior living space"></div>
    <div class="photo villa" role="img" aria-label="Photo of a luxury villa lobby"></div>
  </div>
  <div class="services">
    <div class="service">
      <div class="brand-name">CORVIMO</div>
      <div class="brand-sub">design</div>
      <ul>
        <li>Villa Interior Design</li><li>Office Interior Design</li><li>Landscape Design</li><li>Retail Interior Design</li><li>Hotel Interior Design</li><li>Shopfitting Interior Design</li><li>Cabinet Interior Design</li><li>Hotel Exterior Design</li><li>Restaurant Interior Design</li>
      </ul>
    </div>
    <div class="service">
      <div class="brand-name">CORVIMO</div>
      <div class="brand-sub">landscaping</div>
      <ul>
        <li>Soft Landscaping</li><li>Irrigation Solutions</li><li>Hard Landscaping</li><li>External Lighting</li><li>Swimming Pool</li><li>&amp; Water Features</li>
      </ul>
    </div>
    <div class="service">
      <div class="brand-name">CORVIMO</div>
      <div class="brand-sub">fitout</div>
      <ul>
        <li>Development Approvals</li><li>Flooring Solutions</li><li>Partitions</li><li>Ceiling Solutions</li><li>MEP Works</li><li>Civil Works</li><li>Joinery</li><li>Glass and Aluminum Works</li><li>Steel Structures</li>
      </ul>
    </div>
    <div class="service">
      <div class="brand-name">CORVIMO</div>
      <div class="brand-sub">maintenance</div>
      <ul>
        <li>AC Repair</li><li>Plumber Services</li><li>Electric Repair</li><li>Carpentry Work</li><li>Masonry Works</li><li>Painting Services</li><li>Cleaning Services</li><li>Emergency Services</li>
      </ul>
    </div>
  </div>
  <div class="ornament" role="img" aria-label="Gold flourish ornament"></div>
</section>

</body>
</html>
```